Website Comps for Famous Southern BBQ Restaurant in Alabama

We need an authentic, brand-focused redesign for a restaurant.

We need an authentic look.
The client really likes this website.
https://pelzerpit.com/

I don't want to see a bunch of crazy colors.
Avoid image sliders on the homepage. I hate those.

Please mockup the following three pages:
Homepage
Interior page (for mockup purposes, you can do an About page)
Menu page

I only need the PSD's; not the website coded.

Here is the current website: www.dunmoresmokehouse.com

https://pelzerpit.com/

Here are some additional stock photos. New photos will be shot, but these may help for your mock-up designs.
https://www.filecrate.net/sh/83kqvtrpe21zwa9/QXM71bTr4-plWnfVoe8KtYjd?dl=0
Updates

I realize we don't have a lot of high-quality photos to work with.Those will be shot.Here are some additional stock photos that may help.https://www.filecrate.net/sh/83kqvtrpe21zwa9/QXM71bTr4-plWnfVoe8KtYjd?dl=0 Added Saturday, June 10, 2017

Target Market(s)

United states

Industry/Entity Type

Restaurant

Number of Pages Required

3 page

Font styles to use
Sans Serif

Colors

Designer to choose colors to be used in the design.

Requirements
Must have
• An authentic look.
• The client really likes this website.
• https://pelzerpit.com/
• It's simple, bold, and vintage at the same time.
• That is what we want.
• Our existing website is
• dunmoresmokehouse.com
Nice to have
• Simplicity. Something that makes the food look good.
• Possibly a background.
• Logo:
• https://www.filecrate.net/s/k58tnwpl3ovza2e/dunmore-smokehouse-ridgeway.png?dl=0
• Here is a sampling of photos for your comps:
• https://www.filecrate.net/sh/61vbqzhoewpxtn4/QLT4b8JKyRmPPwf6c2ZnHUVpe?dl=0
Should not have
• Nothing too busy.
• Not too many colors.
• Keep it simple, authentic, "down home."
• No homepage image sliders.

```html
<!DOCTYPE html>
<html lang="en">
<head>
<meta charset="utf-8">
<title>Dunmore Smokehouse – Blog &amp; Footer</title>
<link href="https://fonts.googleapis.com/css2?family=Oswald:wght@500;600&family=Lato:wght@400;700&display=swap" rel="stylesheet">
<style>
  :root{
    --paper:#ffffff;
    --maroon:#4a170c;
    --brick:#7e1c0c;
    --amber:#f5a00f;
    --ink:#666666;
    --meta:#a9a9a9;
    --footer:#232323;
    --footer-deep:#0d0d0d;
    --light:#f2f2f2;
    --muted:#8a8a8a;
  }
  *{margin:0;padding:0;box-sizing:border-box}
  html,body{width:1200px;height:653px;overflow:hidden;background:var(--paper);font-family:"Lato",sans-serif}
  .page{position:relative;width:1200px;height:653px}
  .abs{position:absolute}

  .ornament{left:527px;top:0;width:147px;height:14px;background:linear-gradient(90deg,transparent,#3a2a22 20%,#3a2a22 80%,transparent);opacity:.55;border-radius:0 0 50% 50%}

  .post-photo{width:217px;height:166px;top:74px}
  .post-photo.ribs{left:147px;background:radial-gradient(circle at 45% 55%,#6a3a26,#2a1712 70%)}
  .post-photo.drink{left:609px;background:radial-gradient(circle at 55% 55%,#d9692e,#7a2a12 45%,#1c0f0b 80%)}
  .post-body{top:72px;width:230px}
  .post-title{font-family:"Oswald",sans-serif;font-weight:600;font-size:14.5px;color:var(--maroon);letter-spacing:.2px}
  .post-meta{display:flex;gap:18px;margin-top:10px;font-size:11.5px;color:var(--meta)}
  .post-meta span{display:flex;align-items:center;gap:4px}
  .post-meta svg{width:11px;height:11px;stroke:var(--meta);fill:none;stroke-width:1.6}
  .post-text{margin-top:12px;font-size:11.5px;line-height:21px;color:var(--ink)}
  .read-more{display:block;margin-top:6px;font-size:12px;font-weight:700;color:var(--amber);text-decoration:none}

  .footer{left:0;top:292px;width:1200px;height:310px;background:var(--footer)}
  .bottom-bar{left:0;top:602px;width:1200px;height:51px;background:var(--footer-deep);text-align:center;line-height:51px;font-size:10px;color:var(--muted)}

  .brand-box{left:146px;top:362px;width:68px;height:68px;background:var(--brick);display:flex;align-items:center;justify-content:center;font-family:"Lato",sans-serif;font-weight:700;font-size:12px;color:var(--amber)}
  .about-title{left:146px;top:455px;font-size:11.5px;font-weight:700;color:var(--amber);letter-spacing:.1px}
  .about-text{left:146px;top:478px;width:220px;font-size:11.5px;line-height:19.6px;color:var(--light)}

  .col-title{top:358px;font-family:"Oswald",sans-serif;font-weight:500;font-size:21px;color:var(--amber)}
  .hours-day{left:416px;font-size:12px;font-weight:700;color:var(--amber)}
  .hours-time{left:416px;font-size:12px;line-height:18.5px;color:var(--light)}
  .icon{width:13px;height:13px;fill:none;stroke:var(--amber);stroke-width:1.4}

  .work-grid{left:645px;top:429px;display:grid;grid-template-columns:repeat(3,65px);grid-auto-rows:57px;gap:4px 3px}
  .work-grid div{background:linear-gradient(135deg,#5a2e1c,#1e1410)}
  .work-grid div:nth-child(2){background:linear-gradient(135deg,#3b6ea8,#1d3c66)}
  .work-grid div:nth-child(3){background:linear-gradient(135deg,#a8362a,#5c4a3e)}
  .work-grid div:nth-child(4){background:linear-gradient(135deg,#9a5a2a,#3a1e12)}
  .work-grid div:nth-child(5){background:linear-gradient(135deg,#b59a6a,#5a4a30)}

  .contact-line{left:900px;font-size:12px;line-height:16.5px;color:var(--light)}
</style>
</head>
<body>
<div class="page">
  <div class="abs ornament" role="img" aria-label="Decorative scroll flourish under section heading"></div>

  <div class="abs post-photo ribs" role="img" aria-label="Photo of smoked ribs with white sauce in a basket"></div>
  <article class="abs post-body" style="left:376px">
    <h3 class="post-title">FUSCE SUSCIPIT DUNMORE</h3>
    <div class="post-meta">
      <span><svg viewBox="0 0 12 12"><circle cx="6" cy="6" r="5"/><path d="M6 3v3l2 1"/></svg>25 Dec, 2016</span>
      <span><svg viewBox="0 0 12 12"><path d="M1 5h2v6H1zM3 5l3-4c1 0 1 1 1 2L6.5 5H10l-1 6H3"/></svg>20</span>
      <span><svg viewBox="0 0 12 12"><path d="M1 2h10v6H5l-3 2V8H1z"/></svg>20</span>
    </div>
    <p class="post-text">Ementum ligula lobortis ege quisque interdum nec tellus onec pretium, enim non sollicitudin congue, dolor turpis faucibus libero, in rhoncus ligula lacus a sem.</p>
    <a class="read-more" href="#">READ MORE....</a>
  </article>

  <div class="abs post-photo drink" role="img" aria-label="Photo of an iced red drink with lime on a bar"></div>
  <article class="abs post-body" style="left:838px">
    <h3 class="post-title">FUSCE SUSCIPIT DUNMORE</h3>
    <div class="post-meta">
      <span><svg viewBox="0 0 12 12"><circle cx="6" cy="6" r="5"/><path d="M6 3v3l2 1"/></svg>25 Dec, 2016</span>
      <span><svg viewBox="0 0 12 12"><path d="M1 5h2v6H1zM3 5l3-4c1 0 1 1 1 2L6.5 5H10l-1 6H3"/></svg>20</span>
      <span><svg viewBox="0 0 12 12"><path d="M1 2h10v6H5l-3 2V8H1z"/></svg>20</span>
    </div>
    <p class="post-text">Ementum ligula lobortis ege quisque interdum nec tellus onec pretium, enim non sollicitudin congue, dolor turpis faucibus libero, in rhoncus ligula lacus a sem.</p>
    <a class="read-more" href="#">READ MORE....</a>
  </article>

  <footer>
    <div class="abs footer"></div>

    <div class="abs brand-box">Dunmore's</div>
    <h4 class="abs about-title">VESTIBULUM EUISMOD TORTOR</h4>
    <p class="abs about-text">EgetPellentesque orci ligula, aliquet id porttitor sed, mattis tristique eros. Nulla vel placerat neque, eu pharetra diam. Aliquam vel metus metus. Suspendisse vitae malesuada turpis.</p>

    <h4 class="abs col-title" style="left:394px">Working Hours</h4>
    <svg class="abs icon" style="left:394px;top:427px" viewBox="0 0 14 14"><circle cx="7" cy="7" r="6"/><path d="M7 3.5V7l2.5 1.5"/></svg>
    <div class="abs hours-day" style="top:424px">Monday To Friday</div>
    <div class="abs hours-time" style="top:444px">8:00 am to 10:00 pm (Breakfast)<br>11:00am to 10:00pm (Lunch/Diner)</div>
    <svg class="abs icon" style="left:394px;top:509px" viewBox="0 0 14 14"><circle cx="7" cy="7" r="6"/><path d="M7 3.5V7l2.5 1.5"/></svg>
    <div class="abs hours-day" style="top:507px">Saturday &amp; Sunday</div>
    <div class="abs hours-time" style="top:527px">10:00am to 11:00 pm (Breakfast)<br>11:00am to 12:00pm (Lunch/Dinner)</div>

    <h4 class="abs col-title" style="left:646px">RECENT WORK</h4>
    <div class="abs work-grid">
      <div role="img" aria-label="Bar taps photo"></div>
      <div role="img" aria-label="Restaurant sign photo"></div>
      <div role="img" aria-label="Painted wall sign photo"></div>
      <div role="img" aria-label="Burger and fries photo"></div>
      <div role="img" aria-label="Sandwich photo"></div>
      <div role="img" aria-label="Dining room interior photo"></div>
    </div>

    <h4 class="abs col-title" style="left:883px">CONTACT US</h4>
    <svg class="abs icon" style="left:883px;top:413px" viewBox="0 0 14 14"><path d="M7 13s4.5-4.5 4.5-7.5a4.5 4.5 0 0 0-9 0C2.5 8.5 7 13 7 13z"/><circle cx="7" cy="5.5" r="1.6"/></svg>
    <div class="abs contact-line" style="top:412px">Ut tincidunt /a1506 amet<br>sollicitudin sapien malesuada</div>
    <svg class="abs icon" style="left:883px;top:473px" viewBox="0 0 14 14"><path d="M3 1.5l2 .5 1 3-1.5 1a7 7 0 0 0 3.5 3.5l1-1.5 3 1 .5 2c-1 1.5-2.5 1.5-4 1A11 11 0 0 1 2 5.5c-.5-1.5-.5-3 1-4z"/></svg>
    <div class="abs contact-line" style="top:471px">5550-318-0274</div>
    <svg class="abs icon" style="left:883px;top:518px" viewBox="0 0 14 14"><rect x="1" y="3" width="12" height="8.5"/><path d="M1 3l6 5 6-5"/></svg>
    <div class="abs contact-line" style="top:515px">info@smokemail.com</div>

    <div class="abs bottom-bar">© 2017 All Rights Reserved. DunmoreSmokehouse.com</div>
  </footer>
</div>
</body>
</html>
```